Business Card design for a company called Tallow Flame NI

I need a business card design for my oil fired boiler servicing company. I have a logo design already and Im just looking that incorporated into the business card design. card details; Tallow Flame NI
Oil Burner Servicing - Mid Ulster Area
Service Engineer - Owen Marsh
Mobile 07751364927
email - Tallow.Flame.NI@hearthmail.example
www.tallowflameni.example
I carry out Servicing, Commissioning, Fault Finding, Warranty Validation
Target Market(s)
home owners with oil fired central heating
Industry/Entity Type
Business
Contact Information for Business Card
Tallow Flame NI
Tell. 07751364927
Web: www.tallowflameni.example
email Tallow.Flame.NI@Hearthmail.Example
Servicing Fault Finding Commissioning Warranty Validation
Look and feel

```html
<!DOCTYPE html>
<html lang="en">
<head>
<meta charset="utf-8">
<title>Tallow Flame NI – Business Card</title>
<link rel="stylesheet" href="https://fonts.googleapis.com/css2?family=Nunito:wght@700;800;900&display=swap">
<style>
  :root{
    --page:#ecebe7;
    --paper:#ffffff;
    --ink:#050505;
    --green:#5cc23c;
    --green-light:#8ee05a;
    --green-dark:#3fa52a;
    --lime:#c8ea3a;
    --strip-text:#0d1a08;
  }
  *{box-sizing:border-box;margin:0;padding:0}
  html,body{width:1200px;height:780px;overflow:hidden;background:var(--page)}
  body{font-family:"Nunito",Arial,sans-serif;position:relative}
  .card{
    position:absolute;left:100px;top:105px;width:1000px;height:570px;
    background:var(--paper);overflow:hidden;
    box-shadow:0 10px 30px rgba(0,0,0,.18);
  }
  .card-shapes{position:absolute;inset:0}
  .brand{position:absolute;left:40px;top:128px;display:flex;align-items:center;gap:22px}
  .brand-dot{width:108px;height:108px;border-radius:50%;background:var(--green);flex:none}
  .brand-name{font-size:60px;font-weight:900;color:var(--green);line-height:1;white-space:nowrap}
  .tagline{position:absolute;left:172px;top:238px;font-size:17px;font-weight:700;color:var(--green);letter-spacing:2.5px;text-transform:uppercase;white-space:nowrap}
  .contact{position:absolute;left:440px;top:366px;color:var(--lime);white-space:nowrap}
  .contact-name{font-size:34px;font-weight:900;line-height:1.1}
  .contact-role{font-size:22px;font-weight:800;line-height:1.3}
  .contact-line{display:flex;align-items:center;gap:10px;font-size:21px;font-weight:800;line-height:1.45}
  .contact-line svg{width:22px;height:22px;flex:none}
  .website{position:absolute;right:40px;top:438px;font-size:21px;font-weight:800;color:var(--green);white-space:nowrap}
  .services{position:absolute;left:385px;top:528px;font-size:17px;font-weight:800;color:var(--strip-text);white-space:nowrap}
  .services .sep{margin:0 4px}
</style>
</head>
<body>
  <article class="card">
    <svg class="card-shapes" viewBox="0 0 1000 570" width="1000" height="570" aria-hidden="true">
      <defs>
        <linearGradient id="strip" x1="0" y1="0" x2="0" y2="1">
          <stop offset="0" stop-color="#8ee05a"/>
          <stop offset="1" stop-color="#3fa52a"/>
        </linearGradient>
      </defs>
      <path class="swoosh-edge" d="M150 570 C210 420 360 370 560 345 C780 318 840 170 880 0 L1000 0 L1000 570 Z" fill="var(--green)" transform="translate(-16 -4)"/>
      <path class="dark-band" d="M150 570 C210 420 360 370 560 345 C780 318 840 170 880 0 L1000 0 L1000 570 Z" fill="var(--ink)"/>
      <path class="service-strip" d="M362 512 L1000 512 L1000 570 L330 570 C336 538 346 516 362 512 Z" fill="url(#strip)"/>
    </svg>

    <div class="brand">
      <span class="brand-dot"></span>
      <span class="brand-name">Tallow Flame NI</span>
    </div>
    <p class="tagline">Oil Burner Servicing - Mid Ulster Area</p>

    <div class="contact">
      <p class="contact-name">Owen Marsh</p>
      <p class="contact-role">Service Engineer</p>
      <p class="contact-line">
        <svg viewBox="0 0 26 26"><rect width="26" height="26" fill="var(--lime)"/><path d="M8 5 L11 5 L12 9 L10 11 C11 13 13 15 15 16 L17 14 L21 15 L21 18 C21 19 20 20 19 20 C12 20 6 14 6 7 C6 6 7 5 8 5 Z" fill="var(--ink)"/></svg>
        <span>07751364927</span>
      </p>
      <p class="contact-line">
        <svg viewBox="0 0 26 26"><rect width="26" height="26" fill="var(--lime)"/><rect x="5" y="7" width="16" height="12" fill="none" stroke="var(--ink)" stroke-width="2"/><path d="M5 7 L13 14 L21 7" fill="none" stroke="var(--ink)" stroke-width="2"/></svg>
        <span>Tallow.Flame.NI@Hearthmail.Example</span>
      </p>
    </div>

    <p class="website">www.tallowflameni.example</p>

    <p class="services">Servicing<span class="sep">|</span>Commissioning<span class="sep">|</span>Fault Finding<span class="sep">|</span>Warranty Validation</p>
  </article>
</body>
</html>
```